Dulwick Medical

Need smart and sleek business cards design for my medical distribution company. use logos attached.

add my details

Harriet Colbeck
Director/Sales Agent
harriet@dulwickmedical.com.au
0461 835 207

```html
<!DOCTYPE html>
<html lang="en">
<head>
<meta charset="UTF-8">
<title>Dulwick Medical — Business Card</title>
<link href="https://fonts.googleapis.com/css2?family=Montserrat:wght@500;700;800&family=Arimo:wght@400&display=swap" rel="stylesheet">
<style>
  :root {
    --backdrop: #2b2c31;
    --navy: #0c2a7a;
    --navy-deep: #071c5c;
    --ink-navy: #112b6b;
    --sky: #2f8fd0;
    --paper: #ffffff;
    --text-dark: #1d1d22;
  }
  * { margin: 0; padding: 0; box-sizing: border-box; }
  html, body { width: 1200px; height: 900px; overflow: hidden; }
  body {
    background: var(--backdrop);
    display: flex;
    flex-direction: column;
    align-items: center;
    justify-content: center;
    gap: 44px;
    font-family: "Montserrat", sans-serif;
  }
  .card {
    width: 620px;
    height: 378px;
    border-radius: 22px;
    position: relative;
    overflow: hidden;
    box-shadow: 0 18px 40px rgba(0,0,0,0.45);
  }

  /* Back */
  .card-back {
    background: linear-gradient(160deg, var(--navy) 0%, var(--navy-deep) 100%);
  }
  .card-back .brand-decoration {
    position: absolute;
    top: 0; right: 0;
    width: 54%;
    height: 100%;
    background: linear-gradient(200deg, rgba(40,80,170,0.45) 0%, rgba(20,50,130,0.15) 60%, rgba(0,0,0,0) 100%);
  }
  .card-back .brand {
    position: absolute;
    left: 44px;
    top: 148px;
    display: flex;
    align-items: center;
    gap: 12px;
    color: var(--paper);
  }

  /* Brand lockup */
  .brand-mark {
    width: 30px;
    height: 30px;
    background: currentColor;
  }
  .brand-name {
    font-weight: 800;
    font-size: 34px;
    letter-spacing: 1px;
    line-height: 1;
    text-transform: uppercase;
  }

  /* Front */
  .card-front {
    background: var(--paper);
    display: flex;
    flex-direction: column;
    align-items: center;
    padding-top: 60px;
  }
  .card-front .brand {
    display: flex;
    align-items: center;
    gap: 12px;
    color: var(--ink-navy);
  }
  .holder-name {
    margin-top: 40px;
    font-weight: 800;
    font-size: 30px;
    color: var(--ink-navy);
    letter-spacing: 0.5px;
    line-height: 1.1;
    text-transform: uppercase;
  }
  .holder-title {
    margin-top: 6px;
    font-weight: 500;
    font-size: 18px;
    color: var(--sky);
    text-transform: uppercase;
  }
  .divider {
    width: 340px;
    height: 2px;
    background: var(--sky);
    margin: 14px 0 16px;
  }
  .contact-line {
    display: flex;
    align-items: center;
    gap: 10px;
    font-family: "Arimo", sans-serif;
    font-size: 19px;
    color: var(--text-dark);
  }
  .contact-line svg { flex: none; }
  .contact-phone { margin-top: 18px; }
</style>
</head>
<body>

  <section class="card card-back" aria-label="Business card back">
    <div class="brand-decoration" role="img" aria-label="Faint large brand mark decoration"></div>
    <div class="brand">
      <span class="brand-mark"></span>
      <span class="brand-name">Dulwick Medical</span>
    </div>
  </section>

  <section class="card card-front" aria-label="Business card front">
    <div class="brand">
      <span class="brand-mark"></span>
      <span class="brand-name">Dulwick Medical</span>
    </div>

    <h1 class="holder-name">Harriet Colbeck</h1>
    <p class="holder-title">Director/Sales Agent</p>

    <p class="contact-line contact-phone">
      <svg width="20" height="18" viewBox="0 0 20 18" aria-hidden="true">
        <path d="M2 6 Q10 0 18 6 L16 9 L13 7.5 L13 5.5 Q10 4.5 7 5.5 L7 7.5 L4 9 Z" fill="#2f8fd0"/>
        <rect x="4" y="9" width="12" height="7" rx="2" fill="#2f8fd0"/>
        <circle cx="10" cy="12.5" r="2" fill="#fff"/>
      </svg>
      0461 835 207
    </p>

    <div class="divider"></div>

    <p class="contact-line contact-email">
      <svg width="24" height="17" viewBox="0 0 24 17" aria-hidden="true">
        <rect x="1" y="1" width="22" height="15" fill="#2f8fd0"/>
        <path d="M1 1 L12 10 L23 1" fill="none" stroke="#fff" stroke-width="1.6"/>
      </svg>
      harriet@dulwickmedical.com.au
    </p>
  </section>

</body>
</html>
```